Blow Dry Bar Business Cards

These cards must be eye catching and modern.
You must be willing to work fast and make changes.

Winner will be offered other projects

Files 1 THIS IS THE STYLE CARDS I AM INTRESTED IN!!!
Please be creative, I am paying for my own eye catching design. I need files to be prisma press ready.

COLORS THAT ARE PAINTED INSIDE MY SHOP:
- - - http://www.brenwickcoatings.example/en/explore-colors/painter/color-selector.html?colors=4007-3C

- - - http://www.tarnellhues.example/color/paint-colors/quiet-harbor-d58-2

I want the business cards sleek and modern if you use the logo please correct imperfections. I added the part that says Blow Dry Bar (see website).
Do not be afraid to separate the blow dryer from the name to make the cards look like the file with the pink elephant.

SHOULD INCLUDE
*Blow Dryer (we are a blow dry bar not a salon we do not cut or color so do not include sheers of any kind)
*BUSINESS NAME: Simply Silken Waves - Blow Dry Bar (PLEASE SEE MY WEBSITE)
* Website: SIMPLYSILKENWAVES.EXAMPLE
*Phone number (555) 014-2763
Updates

Prisma press said it can be submitted in JPG

http://www.tarnellhues.example/color/paint-colors/quiet-harbor-d58-2 http://www.brenwickcoatings.example/en/explore-colors/painter/color-selector.html?colors=4007-3C ^^^^ These links will take you to the color paint that is painted inside my shop.

Target Market(s)

AGES 18 - 55 WOMEN
HIGH END MARKET

Industry/Entity Type

Salon

Requirements
Must have
• SEE COLOR EXAMPLE FILE
BLOW DRYER
UNIQUE
I LIKE THE CARD WITH THE PINK ELEPHANT THE BEST
Nice to have
• BE AS CREATIVE AND MODERN AS POSSIBLE DO NOT COPY ANY OF THE CARDS BELOW.
Should not have
• SCISSORS
PINK

```html
<!DOCTYPE html>
<html lang="en">
<head>
<meta charset="utf-8">
<title>Simply Silken Waves – Blow Dry Bar Business Cards</title>
<link href="https://fonts.googleapis.com/css2?family=Montserrat:wght@700&family=Open+Sans:wght@400&display=swap" rel="stylesheet">
<style>
  :root {
    --backdrop: #e6e4e1;
    --card-dark: #3a3b3b;
    --card-light: #f1f1f1;
    --ink-light: #ededed;
    --ink-dark: #4a4a4a;
    --ink-soft: #5a5a5a;
    --divider: #d2d2d2;
    --wave-tone: #5b5e5e;
    --shadow: rgba(0, 0, 0, 0.18);
  }
  * { box-sizing: border-box; margin: 0; padding: 0; }
  html, body {
    width: 1200px;
    height: 900px;
    overflow: hidden;
    background: var(--backdrop);
  }
  .canvas {
    width: 1200px;
    height: 900px;
    display: flex;
    align-items: center;
    justify-content: center;
    gap: 56px;
  }
  .card {
    position: relative;
    width: 520px;
    height: 297px;
    border-radius: 22px;
    box-shadow: 0 10px 28px var(--shadow);
    overflow: hidden;
  }

  /* Shared lockup: name in one weight and colour, plain circle beside it */
  .lockup {
    display: flex;
    align-items: center;
    font-family: "Montserrat", sans-serif;
    font-weight: 700;
    line-height: 1;
  }
  .lockup-name { display: flex; flex-direction: column; }
  .lockup-mark { border-radius: 50%; flex: none; }

  /* Front of card */
  .card-front { background: var(--card-dark); }
  .front-waves {
    position: absolute;
    left: 120px;
    top: 30px;
    width: 280px;
    height: 80px;
    border-radius: 40px;
    background: linear-gradient(90deg, transparent, var(--wave-tone) 45%, transparent);
    opacity: 0.55;
  }
  .front-lockup {
    position: absolute;
    left: 34px;
    bottom: 46px;
    gap: 22px;
    color: var(--ink-light);
  }
  .front-lockup .name-small { font-size: 24px; margin-left: 60px; }
  .front-lockup .name-large { font-size: 48px; letter-spacing: -1px; margin: 4px 0 8px; }
  .front-lockup .name-tag { font-size: 24px; align-self: flex-end; }
  .front-lockup .lockup-mark {
    width: 104px;
    height: 104px;
    background: var(--ink-light);
    margin-bottom: 20px;
  }

  /* Back of card */
  .card-back { background: var(--card-light); display: flex; }
  .back-half {
    width: 50%;
    height: 100%;
    display: flex;
    flex-direction: column;
    justify-content: center;
  }
  .back-brand { align-items: center; border-right: 1px solid var(--divider); }
  .back-lockup { gap: 10px; color: var(--ink-dark); }
  .back-lockup .name-small { font-size: 12px; margin-left: 22px; }
  .back-lockup .name-large { font-size: 23px; letter-spacing: -0.5px; margin: 2px 0 3px; }
  .back-lockup .name-tag { font-size: 12px; align-self: flex-end; }
  .back-lockup .lockup-mark {
    width: 42px;
    height: 42px;
    background: var(--ink-dark);
  }
  .back-contact {
    padding-left: 32px;
    font-family: "Open Sans", sans-serif;
    font-size: 12.5px;
    color: var(--ink-soft);
    letter-spacing: 0.4px;
    line-height: 1.45;
  }
  .contact-phone,
  .contact-web { margin-bottom: 6px; }
  .contact-address { text-transform: uppercase; }
</style>
</head>
<body>
  <main class="canvas">
    <section class="card card-front" aria-label="Business card front">
      <div class="front-waves" role="img" aria-label="Flowing air waves graphic"></div>
      <h1 class="lockup front-lockup">
        <span class="lockup-name">
          <span class="name-small">Simply</span>
          <span class="name-large">Silken Waves</span>
          <span class="name-tag">blow dry bar</span>
        </span>
        <span class="lockup-mark" role="img" aria-label="Blow dryer graphic"></span>
      </h1>
    </section>

    <section class="card card-back" aria-label="Business card back">
      <div class="back-half back-brand">
        <p class="lockup back-lockup">
          <span class="lockup-name">
            <span class="name-small">Simply</span>
            <span class="name-large">Silken Waves</span>
            <span class="name-tag">blow dry bar</span>
          </span>
          <span class="lockup-mark" role="img" aria-label="Blow dryer graphic"></span>
        </p>
      </div>
      <div class="back-half back-contact">
        <p class="contact-phone">(555) 014 - 2763</p>
        <p class="contact-web">SIMPLYSILKENWAVES.EXAMPLE</p>
        <p class="contact-address">208 Harbor Bend Drive Suite<br>4 Willow Creek, Texas 75099</p>
      </div>
    </section>
  </main>
</body>
</html>
```